Statonary for Design Build Firm
Design Build company
Statonary for Design Build Firm -
Creative Brief
Professional
Peter L. Vondrasek
C.E.O.
Doha Qatar
US# 1-415-372-9054
mvelondrask@tmwrgroup.net
www.tmwrgroup.net

```html
<!DOCTYPE html>
<html lang="en">
<head>
<meta charset="utf-8">
<title>TMWR Group – Business Card</title>
<link href="https://fonts.googleapis.com/css2?family=Open+Sans:wght@400;600;700;800&display=swap" rel="stylesheet">
<style>
  :root {
    --page-bg: #e9e6e2;
    --card-bg: #ffffff;
    --brand-blue: #1d5f9e;
    --brand-blue-dark: #123e6e;
    --brand-blue-light: #3a8fd0;
    --accent-orange: #ee7d1e;
    --ink-dark: #3a3a3a;
    --ink-grey: #6d6d6d;
  }
  * { box-sizing: border-box; margin: 0; padding: 0; }
  html, body {
    width: 1200px; height: 1030px; overflow: hidden;
    background: var(--page-bg);
    font-family: "Open Sans", Arial, sans-serif;
  }
  .card {
    position: absolute; left: 100px; top: 225px;
    width: 1000px; height: 580px;
    background: var(--card-bg);
    border-radius: 26px;
    overflow: hidden;
    box-shadow: 0 10px 30px rgba(0,0,0,.18);
  }
  .card__panel { position: absolute; left: 0; top: 0; width: 260px; height: 580px; }
  .brand {
    position: absolute; left: 112px; top: 78px;
    display: flex; align-items: center; gap: 16px;
  }
  .brand__mark { width: 52px; height: 52px; background: var(--brand-blue-light); flex: none; }
  .brand__name {
    font-size: 44px; font-weight: 800; color: var(--ink-dark);
    letter-spacing: -1px; line-height: 1; white-space: nowrap;
  }
  .brand__tagline {
    position: absolute; left: 180px; top: 140px;
    font-size: 14px; font-weight: 600; color: var(--accent-orange);
    white-space: nowrap;
  }
  .person { position: absolute; right: 60px; top: 150px; text-align: right; }
  .person__name { font-size: 36px; font-weight: 400; color: var(--brand-blue); line-height: 1.2; white-space: nowrap; }
  .person__title { font-size: 18px; color: var(--ink-grey); margin-top: 4px; }
  .office {
    position: absolute; top: 350px; text-align: right;
    font-size: 17px; line-height: 1.55; color: var(--accent-orange);
    white-space: nowrap;
  }
  .office--doha { right: 440px; }
  .office--muscat { right: 60px; }
  .office__city { color: var(--ink-dark); font-weight: 600; }
  .office__web { font-weight: 700; }
</style>
</head>
<body>
  <div class="card">
    <svg class="card__panel" viewBox="0 0 260 580" aria-hidden="true">
      <defs>
        <linearGradient id="panelBlue" x1="0" y1="0" x2="1" y2="1">
          <stop offset="0" stop-color="#3a8fd0"/>
          <stop offset="0.55" stop-color="#1d5f9e"/>
          <stop offset="1" stop-color="#123e6e"/>
        </linearGradient>
      </defs>
      <path d="M0 0 H70 L180 580 H0 Z" fill="url(#panelBlue)"/>
      <path d="M70 0 L180 580" stroke="#ee7d1e" stroke-width="6" fill="none"/>
    </svg>

    <div class="brand">
      <div class="brand__mark"></div>
      <div class="brand__name">TMWR GROUP</div>
    </div>
    <div class="brand__tagline">Integrated Design Build Group</div>

    <div class="person">
      <div class="person__name">Peter L. Vondrasek</div>
      <div class="person__title">Chief Executive Officer</div>
    </div>

    <div class="office office--doha">
      <div class="office__city">Doha Qatar</div>
      <div>Doha Office: +974 (0)50-218-4476</div>
      <div>Email: mvelondrask@tmwrgroup.net</div>
      <div>skype: mvelondrask</div>
      <div class="office__web">www.tmwrgroup.net</div>
    </div>

    <div class="office office--muscat">
      <div class="office__city">Muscat Oman</div>
      <div>Muscat Office: +968-78-3105-6627</div>
      <div>Email: mvelondrask@tmwrgroup.net</div>
      <div>skype: mvelondrask</div>
      <div class="office__web">www.tmwrgroup.net</div>
    </div>
  </div>
</body>
</html>
```